QRV Stationery Design Project

Dear Designers,
We need a new stationery design for company to match our new logo.
Designers should provide a design for the following:
1. Business Card: 3.5x2 Inches.
2. Letterhead: A4 size.
3. Envelops: 25x35.5 Cm.
You can keep the Arabic name at the bottom of the logo Or you can use the separate attached Arabic Name.
Please refer to the attached logo guide for design information.
Sample Business Card information:
Name: Tariq Nawaf
Position: Operation Manager
Tel: +966 920007714 Ex. 500
Fax: +966 (3)8842617
Mob: +966 (5)00387251
email: tariq@qrv-example.com.sa
URL: www.qrv-example.com.sa
Address:
Al Wadi Tower, Suite 303
Nasser bin Salem Str.
Khobar, 31847
Saudi Arabia
Updates
Dear All,
Please note, we had uploaded our logo along with Arabic writing in Adobe illustrator format (.ai).
Regards,
Khalid
Dear All,
A sample data for the business card had been added as per your request.
Regards,
Khalid

```html
<!DOCTYPE html>
<html lang="en">
<head>
<meta charset="utf-8">
<title>QRV Letterhead</title>
<link rel="stylesheet" href="https://fonts.googleapis.com/css2?family=Ubuntu:wght@400;700&display=swap">
<style>
  :root {
    --navy: #14385a;
    --ink: #1a1a1a;
    --paper: #ffffff;
    --edge: #8a8a8a;
  }
  html, body {
    margin: 0;
    padding: 0;
    overflow: hidden;
    background: var(--paper);
  }
  .letterhead {
    position: relative;
    width: 848px;
    height: 1200px;
    box-sizing: border-box;
    border: 1px solid var(--edge);
    background: var(--paper);
    overflow: hidden;
    font-family: "Ubuntu", sans-serif;
    color: var(--ink);
  }
  .satellite-art {
    position: absolute;
    left: 20px;
    top: 24px;
    width: 166px;
    height: 88px;
  }
  .brand {
    position: absolute;
    right: 52px;
    top: 72px;
    display: flex;
    align-items: center;
    gap: 12px;
  }
  .brand-mark {
    width: 20px;
    height: 20px;
    background: var(--navy);
  }
  .brand-name {
    font-size: 52px;
    font-weight: 700;
    color: var(--navy);
    letter-spacing: 2px;
    line-height: 1;
  }
  .footer-band {
    position: absolute;
    left: 534px;
    bottom: 0;
    width: 314px;
    height: 90px;
  }
  .vehicle-art {
    position: absolute;
    left: 692px;
    top: 1076px;
    width: 136px;
    height: 124px;
  }
  .contact {
    position: absolute;
    left: 42px;
    top: 1091px;
    margin: 0;
    font-style: normal;
    font-size: 11.5px;
    line-height: 18px;
  }
  .contact .company {
    font-size: 13px;
  }
  .contact .web {
    font-size: 13.5px;
  }
</style>
</head>
<body>
  <main class="letterhead">
    <svg class="satellite-art" role="img" aria-label="Satellite with signal waves illustration" viewBox="0 0 166 88">
      <rect x="-6" y="33" width="178" height="22" rx="3" fill="var(--navy)" transform="rotate(-27 83 44)"/>
    </svg>

    <div class="brand">
      <span class="brand-mark"></span>
      <span class="brand-name">QRV</span>
    </div>

    <svg class="footer-band" viewBox="0 0 314 90" preserveAspectRatio="none" aria-hidden="true">
      <polygon points="0,90 314,90 314,0" fill="var(--navy)"/>
    </svg>
    <svg class="vehicle-art" role="img" aria-label="Truck with tracking antenna illustration" viewBox="0 0 136 124">
      <rect width="136" height="124" fill="var(--navy)"/>
    </svg>

    <address class="contact">
      <div class="company">QRV Tracking Technologies</div>
      <div>Unit 2, Sample Building, Example Business Park, Any City, 00000</div>
      <div>Tel: 000 0000 0000&nbsp; Fax: 000 0000 0001&nbsp; Email: info@example-tracking.com</div>
      <div class="web">www.example-tracking.com</div>
    </address>
  </main>
</body>
</html>
```